Simple elegant feminine design - Going out on my own as a Mortgage Broker.
My thoughts are the following details on the Front, middle of the card possibly? Phone and email smaller font than my name?
Marnie Veltrin
Finance Specialist
p: 0438 215 962
e: marnie@veltrinlending.com.au
Bottom of the card
residential / commercial / equipment
I would like the Font in Rose Gold maybe white or black background? or Possibly a stone grey - are you able to do a few options? I'd like them embossed
Then I had an idea as a simple logo as per the attached if you get the idea in my scribble, my initials, capital M attached to a small v that leads/follows into a circle? Thicker Font In Rose Gold, middle of the card at the back.
Very open to ideas though and what colour you think would look better with the Rose Gold.
Thanks so much for your help, I am not very creative and savvy with this stuff :-)
Industry/Entity Type
Finance
Contact Information for Business Card
Marnie Veltrin
p: 0438 215 962
Look and feel

```html
<!DOCTYPE html>
<html lang="en">
<head>
<meta charset="utf-8">
<title>Marnie Veltrin Business Cards</title>
<link rel="stylesheet" href="https://fonts.googleapis.com/css2?family=Anonymous+Pro:ital@1&family=Cinzel&display=swap">
<style>
  :root {
    --stage: #252527;
    --card: #f7dbcb;
    --rose: #e7a393;
    --rose-soft: #eeb0a2;
    --stone: #8d9193;
    --panel: #cfd3d3;
    --swatch-1: #e6a895;
    --swatch-2: #fbdccd;
    --swatch-3: #fde9dd;
    --swatch-4: #f6b8aa;
    --swatch-5: #8f9495;
  }
  * { margin: 0; padding: 0; box-sizing: border-box; }
  html, body { width: 1200px; height: 1200px; overflow: hidden; background: var(--stage); }
  .board { position: relative; width: 1200px; height: 1200px; }

  .palette {
    position: absolute; left: 803px; top: 6px; width: 266px; height: 94px;
    background: var(--panel); border: 2px solid #e4e6e6;
  }
  .palette-title {
    position: absolute; top: 12px; width: 100%; text-align: center;
    font: 12px "Cinzel", serif; letter-spacing: 3px; color: #3a3d3f;
  }
  .palette-swatches { position: absolute; left: 9px; top: 35px; display: flex; }
  .palette-swatches span { width: 49px; height: 49px; }

  .card {
    position: absolute; left: 234px; width: 736px; height: 420px;
    background: var(--card);
    box-shadow: 0 26px 34px rgba(0,0,0,.55);
  }
  .card-front { top: 126px; }
  .card-back { top: 651px; }

  .type {
    position: absolute; left: 0; width: 100%; text-align: center;
    font-family: "Anonymous Pro", monospace; font-style: italic;
    color: var(--rose); white-space: nowrap;
  }
  .name { top: 112px; left: 18px; font-size: 38px; font-variant: small-caps; letter-spacing: 7px; }
  .name-rule { position: absolute; left: 176px; top: 166px; width: 412px; height: 2px; background: var(--rose); }
  .title { top: 186px; left: 14px; font-size: 22px; font-variant: small-caps; letter-spacing: 4px; color: var(--rose-soft); }
  .phone { top: 244px; left: 12px; font-size: 26px; letter-spacing: 3px; color: var(--rose-soft); }
  .email { top: 284px; left: 4px; font-size: 19px; text-transform: uppercase; letter-spacing: 3px; color: var(--rose-soft); }
  .services { top: 397px; left: 4px; font-size: 11px; text-transform: uppercase; letter-spacing: 7px; color: var(--stone); }

  .brand-mark { position: absolute; left: 246px; top: 89px; }
  .brand-name {
    top: 200px; font-size: 22px; font-variant: small-caps; letter-spacing: 3px;
  }
</style>
</head>
<body>
<main class="board">
  <aside class="palette">
    <p class="palette-title">COLOR IN USE</p>
    <div class="palette-swatches">
      <span style="background:var(--swatch-1)"></span>
      <span style="background:var(--swatch-2)"></span>
      <span style="background:var(--swatch-3)"></span>
      <span style="background:var(--swatch-4)"></span>
      <span style="background:var(--swatch-5)"></span>
    </div>
  </aside>

  <section class="card card-front">
    <h1 class="type name">Marnie Veltrin</h1>
    <div class="name-rule"></div>
    <p class="type title">Finance Specialist</p>
    <p class="type phone">0438 215 962</p>
    <p class="type email">marnie@veltrinlending.com.au</p>
    <p class="type services">residential / commercial / equipment</p>
  </section>

  <section class="card card-back">
    <svg class="brand-mark" width="244" height="244" viewBox="0 0 244 244" aria-hidden="true">
      <circle cx="122" cy="122" r="120" fill="none" stroke="var(--rose-soft)" stroke-width="2"/>
    </svg>
    <p class="type brand-name">Veltrin Lending</p>
  </section>
</main>
</body>
</html>
```